Very new and innovative Web design for Property managers of Vacation rentals

We are looking for a new website design for travel agencies and property managers specialised on vacation rentals business, holiday villas and apartments.

The end users of this website are travellers who are looking for a vacation home for their next holiday: this is the reason why the website must be easy to use, attractive, professional, possibly elegant and focused on get new reservations.

This is a draft of our current website: https://demo5.holdiquay.com/
Please consider that we would like to have proposals with a totally different and innovative layout, surprise us!

These are the pages of the website:
• Homepage: feel free to redesign all the homepage as you wish, surprise us with something very new! Please consider that Property manager/Travel agencies usually want to have the opportunity to put in evidence groups of houses with specific characteristics (eg. villas with private swimming pool, apartment in big/small towns, villas with air co, etc…), destinations and tourist areas, and sometimes experiences or activities (please consider that the website layout must be suitable even if some of the previous sections are not used).
• Search page: we’d like to organise the results of the search page in three different ways:
o Grid
o Map
o List
• Property page: to illustrate the characteristics, descriptions, images, …. of the property. It is very important to put in evidence images of the property and to maintain the booking form (and the other call to action bottom – eg. whatsapp) always visible
• Custom pages: static pages composed usually by text, images and call to actions
• Contact us (general form)
• Info request (specific of a property form)
• Booking process
• Blog, organised in four pages:
o Home Page – introduction to the blog
o List of articles
o Single article
o Site Map (presentation of categories and sub-categories)

If possible, we’d prefer to receive the material in Adobe XD or similar so that we can obtain the three versions:
- smartphone
- tablet
- desktop

The website will be then developed in Bootstrap: as a result we’ll need the icons in SVG format (or the library used)

In attachment you can find the map of the website pages

```html
<!DOCTYPE html>
<html lang="en">
<head>
<meta charset="utf-8">
<title>StayNest – Exclusive Villas in Italy</title>
<link href="https://fonts.googleapis.com/css2?family=Playfair+Display:wght@400;700&family=Lato:wght@400;700&display=swap" rel="stylesheet">
<style>
:root{
  --green:#17bf8b;
  --green-dark:#10a877;
  --ink:#1f2623;
  --dark:#222a27;
  --footer:#1b1f1e;
  --text:#4a4f4d;
  --muted:#8a8f8d;
  --soft:#f3f5f4;
  --line:#d8dcda;
  --white:#ffffff;
}
*{box-sizing:border-box;margin:0;padding:0}
html,body{width:1200px;height:5199px;overflow:hidden}
body{font-family:"Lato",sans-serif;color:var(--text);background:var(--white);position:relative}
.abs{position:absolute}
.serif{font-family:"Playfair Display",serif}
.btn{display:inline-flex;align-items:center;justify-content:center;background:var(--green);color:var(--white);font-family:"Lato",sans-serif;font-weight:700;font-size:12px;letter-spacing:.5px;text-transform:uppercase;border:0}
.photo{display:block}

/* header */
.topbar{left:848px;top:0;width:352px;height:40px;background:var(--green);display:flex;align-items:center;justify-content:flex-end;gap:28px;padding-right:60px;color:var(--white);font-size:11px;font-weight:700}
.topbar span{display:flex;align-items:center;gap:6px}
.logo{display:flex;align-items:center;gap:8px;font-size:27px;color:var(--ink);font-weight:400}
.logo i{width:30px;height:30px;background:var(--green);display:block}
.header-logo{left:113px;top:28px}
.nav{font-size:12px;color:var(--ink)}
.nav a{color:inherit;text-decoration:none;text-transform:uppercase;position:absolute;white-space:nowrap;transform:translateX(-50%)}
.nav a.active{color:var(--green)}

/* hero */
.hero{left:0;top:91px;width:1200px;height:516px;background:linear-gradient(180deg,#5f7d86 0%,#3f5a55 40%,#24302c 75%,#2f2a22 100%)}
.hero-kicker{left:113px;top:318px;font-size:36px;color:var(--white)}
.hero-title{left:113px;top:352px;font-size:64px;font-weight:700;color:var(--white);line-height:1}
.hero-text{left:113px;top:430px;width:430px;font-size:13px;line-height:22px;color:var(--white)}
.search{left:672px;top:246px;width:417px;height:361px;background:rgba(235,237,236,.94);padding:30px 28px}
.search h2{font-family:"Playfair Display",serif;font-weight:400;font-size:24px;color:var(--ink);margin-bottom:22px}
.field{height:46px;background:var(--white);border:1px solid var(--line);display:flex;align-items:center;justify-content:space-between;padding:0 14px;font-size:11px;font-weight:700;letter-spacing:.5px;color:var(--ink)}
.field-row{display:flex;gap:10px;margin:16px 0}
.field-row .field{flex:1}
.search .btn{width:100%;height:49px;margin-top:16px;font-size:14px;text-transform:none;letter-spacing:.3px}

/* sections */
.pattern{background:var(--soft)}
.section-title{width:1200px;left:0;text-align:center;font-family:"Playfair Display",serif;font-weight:700;color:var(--ink);font-size:40px}
.section-sub{width:1200px;left:0;text-align:center;font-size:13px;color:var(--ink)}
.trio{left:113px;width:974px;display:grid;grid-template-columns:307px 307px 306px;column-gap:27px}
.caption{font-family:"Playfair Display",serif;font-size:19px;color:var(--ink);text-align:center;margin-top:18px}

/* holiday */
.holiday-dark{left:0;top:1200px;width:1004px;height:652px;background:var(--dark)}
.holiday-green{left:1004px;top:1200px;width:196px;height:652px;background:var(--green)}
.holiday-kicker{left:113px;top:1290px;font-size:16px;color:var(--white)}
.holiday-title{left:113px;top:1310px;font-size:40px;font-weight:700;color:var(--white)}
.holiday-text{left:113px;top:1366px;width:830px;font-size:13px;line-height:24px;color:#c9cecc}

/* destinations */
.dest{display:flex;flex-direction:column}
.dest h3{font-family:"Playfair Display",serif;font-weight:400;font-size:19px;color:var(--ink);margin-top:18px}
.dest p{font-size:12px;line-height:19px;color:var(--muted);margin-top:8px;width:300px}
.dest .btn{width:103px;height:33px;margin-top:20px;font-size:11px}

/* rentals */
.rentals{left:0;top:3122px;width:1200px;height:283px;display:grid;grid-template-columns:300px 300px 300px 300px}
.rental-feature{position:relative;background:linear-gradient(180deg,#2a2d2b 0%,#3b403d 55%,#2e312f 100%)}
.rental-feature h4{position:absolute;left:19px;top:132px;font-family:"Playfair Display",serif;font-weight:700;font-size:21px;color:var(--white);white-space:nowrap}
.rental-feature dl{position:absolute;left:19px;top:172px;width:120px;font-size:13px;color:#e6e9e8;display:grid;grid-template-columns:1fr auto;row-gap:4px}
.rental-feature .btn{position:absolute;left:19px;top:226px;width:103px;height:37px;font-size:11px}

/* experiences */
.exp-head{left:0;top:3472px;width:535px;text-align:right;color:var(--ink);font-family:"Playfair Display",serif}
.exp-head small{display:block;font-size:20px}
.exp-head strong{display:block;font-size:40px;font-weight:700;line-height:42px;margin-top:2px}
.exp-rule{left:599px;top:3480px;width:1px;height:100px;background:var(--line)}
.exp-intro{left:672px;top:3506px;width:400px;font-size:13px;line-height:21px;color:var(--text)}
.feature{display:flex;gap:17px;width:440px}
.feature .icon{width:64px;height:64px;border-radius:50%;background:var(--green);flex:none;display:flex;align-items:center;justify-content:center}
.feature h5{font-family:"Playfair Display",serif;font-weight:400;font-size:20px;color:var(--ink)}
.feature p{font-size:12px;line-height:18px;color:var(--muted);margin-top:4px}

/* blog */
.blog h3{font-family:"Playfair Display",serif;font-weight:400;font-size:19px;line-height:26px;color:var(--ink);margin-top:18px}
.blog .btn{width:103px;height:34px;margin-top:14px;font-size:11px}

/* contact */
.input{border:1px solid var(--line);background:var(--white);font-size:11px;color:var(--muted);padding:0 14px;display:flex;align-items:center}
.input.area{align-items:flex-start;padding-top:16px}

/* footer */
.footer{left:0;top:4871px;width:1200px;height:328px;background:var(--footer)}
.footer-logo{left:113px;top:4993px;color:var(--green);font-size:25px}
.fcol{color:#b7bcba;font-size:12px}
.fcol h6{font-family:"Playfair Display",serif;font-weight:400;font-size:18px;color:var(--white);margin-bottom:16px}
.fcol li{list-style:none;margin-bottom:13px}
.contact-line{display:flex;gap:10px;margin-bottom:18px;line-height:17px}
.social{display:flex;align-items:center;gap:12px;margin-bottom:13px}
.social i{width:26px;height:26px;border-radius:50%;background:var(--white);display:block}
.copyright{left:0;top:5124px;width:1200px;text-align:center;font-size:11px;color:#9aa09e}
.copyright b{color:var(--white)}
</style>
</head>
<body>

<!-- header -->
<div class="abs topbar">
  <span><svg width="12" height="12" viewBox="0 0 12 12"><circle cx="6" cy="4" r="2.6" fill="none" stroke="#fff" stroke-width="1.3"/><path d="M1.5 11.5c.5-3 2.2-4 4.5-4s4 1 4.5 4" fill="none" stroke="#fff" stroke-width="1.3"/></svg>LOGIN</span>
  <span><svg width="13" height="12" viewBox="0 0 13 12"><path d="M6.5 11 1.6 6.1A2.9 2.9 0 0 1 6.5 2a2.9 2.9 0 0 1 4.9 4.1Z" fill="none" stroke="#fff" stroke-width="1.3"/></svg>WHISHLIST</span>
  <span>EN <svg width="8" height="6" viewBox="0 0 8 6"><path d="m1 1 3 3 3-3" fill="none" stroke="#fff" stroke-width="1.3"/></svg></span>
</div>
<div class="abs logo header-logo"><i></i>StayNest</div>
<nav class="abs nav" style="left:0;top:62px">
  <a class="active" style="left:589px">Home</a>
  <a style="left:690px">Search</a>
  <a style="left:805px">Property</a>
  <a style="left:922px">Custom</a>
  <a style="left:1047px">Contact Us</a>
</nav>

<!-- hero -->
<div class="abs hero photo" role="img" aria-label="Lakeside alpine village with church spire, mountains and water at dusk"></div>
<div class="abs hero-kicker serif">Exclusive</div>
<h1 class="abs hero-title serif">Villas in Italy</h1>
<p class="abs hero-text">Our vacation homes are all located in Italy and we take care of them and their owners at every time.</p>
<form class="abs search">
  <h2>Exclusive Villas in Italy</h2>
  <div class="field">Destination<svg width="16" height="20" viewBox="0 0 16 20"><path d="M8 1a6.5 6.5 0 0 0-6.5 6.5C1.5 12 8 19 8 19s6.5-7 6.5-11.5A6.5 6.5 0 0 0 8 1Z" fill="none" stroke="#1f2623" stroke-width="2"/><circle cx="8" cy="7.5" r="2.3" fill="#1f2623"/></svg></div>
  <div class="field-row">
    <div class="field">Check In<svg width="16" height="15" viewBox="0 0 16 15"><rect x="1" y="2.5" width="14" height="11.5" fill="none" stroke="#1f2623" stroke-width="1.5"/><path d="M1 6h14M4.5 1v3M11.5 1v3" stroke="#1f2623" stroke-width="1.5"/><rect x="4" y="8.5" width="3" height="2.5" fill="#1f2623"/></svg></div>
    <div class="field">Check Out<svg width="16" height="15" viewBox="0 0 16 15"><rect x="1" y="2.5" width="14" height="11.5" fill="none" stroke="#1f2623" stroke-width="1.5"/><path d="M1 6h14M4.5 1v3M11.5 1v3" stroke="#1f2623" stroke-width="1.5"/><rect x="4" y="8.5" width="3" height="2.5" fill="#1f2623"/></svg></div>
  </div>
  <div class="field">Travelers<svg width="14" height="15" viewBox="0 0 14 15"><circle cx="7" cy="4.5" r="3" fill="none" stroke="#1f2623" stroke-width="1.5"/><path d="M1.5 14c0-3 2.4-5 5.5-5s5.5 2 5.5 5Z" fill="none" stroke="#1f2623" stroke-width="1.5"/></svg></div>
  <button type="button" class="btn">Search Now</button>
</form>

<!-- best opportunity -->
<div class="abs pattern" style="left:0;top:607px;width:1200px;height:593px"></div>
<h2 class="abs section-title" style="top:694px">Best Opportunity</h2>
<p class="abs section-sub" style="top:754px">To put in Evidence groups of Houses with Specific Characteristics</p>
<div class="abs trio" style="top:797px">
  <figure><div class="photo" role="img" aria-label="Guest relaxing by a private swimming pool" style="height:266px;background:linear-gradient(160deg,#d9c8a8 0%,#e8d6c4 35%,#8fd0d9 70%,#4fb3c6 100%)"></div><figcaption class="caption">Private Swimming Pool</figcaption></figure>
  <figure><div class="photo" role="img" aria-label="Canal street with bridge and apartments in a town" style="height:266px;background:linear-gradient(180deg,#a9b8c2 0%,#8a7f72 45%,#6b6259 75%,#5d6b70 100%)"></div><figcaption class="caption">Apartment in Big/Small Towns</figcaption></figure>
  <figure><div class="photo" role="img" aria-label="Bedroom with large window overlooking the sea" style="height:266px;background:linear-gradient(180deg,#8fa2b0 0%,#6e7a82 40%,#4a4b4b 70%,#c9c6c0 100%)"></div><figcaption class="caption">Villas with Air Conditions</figcaption></figure>
</div>

<!-- exclusive holiday -->
<div class="abs holiday-dark"></div>
<div class="abs holiday-green"></div>
<div class="abs holiday-kicker serif">Looking for an</div>
<h2 class="abs holiday-title serif">Exclusive Holiday?</h2>
<p class="abs holiday-text">Browse our vacation rental selections If you are looking for a real experiences, our portal is the right solution. Our vacation homes are all located in Italy and we take care of them and their owners at every time. Our goal is give to our guest authentic taste of holiday and our country. Our team is always ready to assure the best time and take care of you! Add a local experience to your stay with us: by diving into our local "network" you can have the unique chance to discover and travel our culture through the eye of a local...!</p>
<div class="abs photo" role="img" aria-label="Clifftop sanctuary above a turquoise sea with boats" style="left:113px;top:1509px;width:974px;height:439px;background:linear-gradient(90deg,#b9ab8d 0%,#6f7f55 28%,#4aa0c4 45%,#8ed1ea 70%,#2e8fbd 100%)"></div>

<!-- destinations -->
<h2 class="abs section-title" style="top:2008px">Destinations &amp; Tourist Areas</h2>
<div class="abs trio" style="top:2084px;row-gap:40px">
  <article class="dest"><div class="photo" role="img" aria-label="Roman Coliseum under blue sky" style="height:264px;background:linear-gradient(180deg,#6fa6d6 0%,#a8c6df 40%,#b58c5e 60%,#7a5a3c 100%)"></div><h3>Roman Coliseum</h3><p>If you use this site regularly and would like to help keep the site on the Internet</p><a class="btn">View More</a></article>
  <article class="dest"><div class="photo" role="img" aria-label="Grand canal with boats and colourful buildings" style="height:264px;background:linear-gradient(180deg,#7fb4e0 0%,#c9a07e 35%,#6f8a86 60%,#3f8b86 100%)"></div><h3>Canal of &nbsp;a City</h3><p>If you use this site regularly and would like to help keep the site on the Internet</p><a class="btn">View More</a></article>
  <article class="dest"><div class="photo" role="img" aria-label="Venice lagoon with domed basilica" style="height:264px;background:linear-gradient(180deg,#b8c7d2 0%,#c4b6a6 45%,#7b8d8f 65%,#5d7c84 100%)"></div><h3>Venice Italy</h3><p>If you use this site regularly and would like to help keep the site on the Internet</p><a class="btn">View More</a></article>
  <article class="dest"><div class="photo" role="img" aria-label="Rock-carved treasury facade in red sandstone" style="height:265px;background:linear-gradient(180deg,#b77a58 0%,#9c5f42 45%,#c08a66 100%)"></div><h3>Petra Uum in Jordan</h3><p>If you use this site regularly and would like to help keep the site on the Internet</p><a class="btn">View More</a></article>
  <article class="dest"><div class="photo" role="img" aria-label="Leaning tower and cathedral under blue sky" style="height:265px;background:linear-gradient(180deg,#3d7fd0 0%,#8fb7e8 45%,#e6e1d6 70%,#6a8a4e 100%)"></div><h3>Tower of &nbsp;Pisa</h3><p>If you use this site regularly and would like to help keep the site on the Internet</p><a class="btn">View More</a></article>
  <article class="dest"><div class="photo" role="img" aria-label="Illuminated basilica at dusk" style="height:265px;background:linear-gradient(180deg,#1f2a4a 0%,#2f3d66 45%,#c9a25e 70%,#4a3a2a 100%)"></div><h3>Vatican Building at Dusk</h3><p>If you use this site regularly and would like to help keep the site on the Internet</p><a class="btn">View More</a></article>
</div>

<!-- new villas -->
<div class="abs pattern" style="left:0;top:3000px;width:1200px;height:122px"></div>
<div class="abs section-sub serif" style="top:3032px;font-size:20px;color:var(--ink)">New Villas &amp;</div>
<h2 class="abs section-title" style="top:3054px">Vacation Rentals</h2>
<div class="abs rentals">
  <div class="photo" role="img" aria-label="Modern villa with infinity pool and palms" style="background:linear-gradient(180deg,#6fa3d6 0%,#d8d4cc 50%,#2f9ed0 80%,#1e7fb1 100%)"></div>
  <div class="photo" role="img" aria-label="White villa with pool and garden" style="background:linear-gradient(180deg,#4f8fd8 0%,#e9e2d6 50%,#3aa9d8 80%,#8c7a5a 100%)"></div>
  <div class="rental-feature" role="img" aria-label="Featured country villa at night">
    <h4>Casale Le Querce</h4>
    <dl><dt>Sleeps</dt><dd>27</dd><dt>Bedrooms</dt><dd>10</dd></dl>
    <a class="btn">View Details</a>
  </div>
  <div class="photo" role="img" aria-label="Guest relaxing in a sunset pool" style="background:linear-gradient(180deg,#d98b4a 0%,#e6b07a 40%,#c97a5a 65%,#3aa8c0 100%)"></div>
</div>

<!-- experiences -->
<div class="abs exp-head"><small>sometimes</small><strong>Experiences or<br>Activities</strong></div>
<div class="abs exp-rule"></div>
<p class="abs exp-intro">Consectetur adipisicing elit, sed do eiusmod tempor incididunt ut labore eusmod tempor incididunt ut labore et dolore. Proin eget tellus tristique lacinia erat non.</p>

<div class="abs feature" style="left:113px;top:3641px">
  <span class="icon"><svg width="30" height="28" viewBox="0 0 30 28"><path d="M3 13 15 3l12 10" fill="none" stroke="#fff" stroke-width="2.2"/><rect x="7" y="12" width="16" height="14" fill="none" stroke="#fff" stroke-width="2.2"/><rect x="12.5" y="18" width="5" height="8" fill="#fff"/></svg></span>
  <div><h5>Luxury Villas</h5><p>This selection of properties includes all the best rentals available. Most with private swimming pool with chef and maid services available.</p></div>
</div>
<div class="abs feature" style="left:670px;top:3641px">
  <span class="icon"><svg width="30" height="30" viewBox="0 0 30 30"><circle cx="15" cy="11" r="7" fill="none" stroke="#fff" stroke-width="2.2"/><path d="M11.5 11l2.5 2.5 4.5-5" fill="none" stroke="#fff" stroke-width="2.2"/><path d="M4 27l6-5h9" fill="none" stroke="#fff" stroke-width="2.2"/></svg></span>
  <div><h5>Browse All Vacation Rentals</h5><p>From here you can browse all the villa selections, you can refine them by using the filters on the search results web page.</p></div>
</div>
<div class="abs feature" style="left:113px;top:3764px">
  <span class="icon"><svg width="32" height="26" viewBox="0 0 32 26"><circle cx="16" cy="7" r="4" fill="#fff"/><circle cx="6" cy="10" r="3" fill="#fff"/><circle cx="26" cy="10" r="3" fill="#fff"/><path d="M9 24c0-5 3-8 7-8s7 3 7 8Z M1 24c0-4 2-7 5-7s4 2 4 3M31 24c0-4-2-7-5-7s-4 2-4 3" fill="#fff"/></svg></span>
  <div><h5>Experiences</h5><p>Don't live just a holiday but an experience! Let's discover our services</p></div>
</div>
<div class="abs feature" style="left:670px;top:3764px">
  <span class="icon"><svg width="32" height="24" viewBox="0 0 32 24"><path d="M2 8h6l6-4 8 0 8 4M2 8v10h5l7 5 6-3 9-8" fill="none" stroke="#fff" stroke-width="2.2" stroke-linejoin="round"/><path d="M14 10l4 3 4-3" fill="none" stroke="#fff" stroke-width="2"/></svg></span>
  <div><h5>Last Minute Deals</h5><p>Browse all the last minute deals to browse the villas offering discounts for last minute arrivals.<br>Save money by checking these offers.</p></div>
</div>

<!-- recent blog -->
<div class="abs pattern" style="left:0;top:3913px;width:1200px;height:545px"></div>
<h2 class="abs section-title" style="top:3958px">Recent Blog</h2>
<div class="abs trio blog" style="top:4034px">
  <article><div class="photo" role="img" aria-label="Guests checking in at a festive reception desk" style="height:220px;background:linear-gradient(135deg,#caa57c 0%,#8a3a2e 45%,#f0ede6 100%)"></div><h3>Quis autem vel eum iure reprehenderit qui in ea voluptate</h3><a class="btn">Read More</a></article>
  <article><div class="photo" role="img" aria-label="Restaurant table set with plates and glasses" style="height:220px;background:linear-gradient(135deg,#e8c9a0 0%,#f5ede2 45%,#c78a4a 100%)"></div><h3>Quis autem vel eum iure reprehenderit qui in ea voluptate</h3><a class="btn">Read More</a></article>
  <article><div class="photo" role="img" aria-label="Seaside resort hotel with pier and pool" style="height:220px;background:linear-gradient(180deg,#6aa6dc 0%,#e8e4dc 45%,#3a8fc0 75%,#2a5f8a 100%)"></div><h3>Quis autem vel eum iure reprehenderit qui in ea voluptate</h3><a class="btn">Read More</a></article>
</div>

<!-- quick contact -->
<h2 class="abs section-title" style="top:4492px">Quick Contact</h2>
<form>
  <div class="abs input" style="left:262px;top:4562px;width:218px;height:41px">Name:</div>
  <div class="abs input" style="left:492px;top:4562px;width:218px;height:41px">Email:</div>
  <div class="abs input" style="left:720px;top:4562px;width:220px;height:41px">Phone:</div>
  <div class="abs input area" style="left:262px;top:4615px;width:678px;height:125px">Message:</div>
  <button type="button" class="abs btn" style="left:835px;top:4756px;width:105px;height:38px">Submit</button>
</form>

<!-- footer -->
<footer class="abs footer"></footer>
<div class="abs logo footer-logo"><i></i>StayNest</div>
<div class="abs fcol" style="left:335px;top:4920px">
  <h6>Quick Links</h6>
  <ul><li>Home</li><li>Search</li><li>Property</li><li>Custom</li><li>Contact Us</li></ul>
</div>
<div class="abs fcol" style="left:526px;top:4920px">
  <h6>Company</h6>
  <ul><li>Privacy Policies</li><li>Reservation Policies</li><li>Cookie Policy</li></ul>
</div>
<div class="abs fcol" style="left:726px;top:4920px;width:220px">
  <h6>Contact Us</h6>
  <div class="contact-line"><svg width="10" height="14" viewBox="0 0 10 14"><path d="M5 0a5 5 0 0 0-5 5c0 3.5 5 9 5 9s5-5.5 5-9a5 5 0 0 0-5-5Z" fill="#fff"/><circle cx="5" cy="5" r="1.8" fill="#1b1f1e"/></svg><span>Via dei Cipressi 7 50100<br>Borgo Verde, Toscana (Italy)</span></div>
  <div class="contact-line"><svg width="12" height="12" viewBox="0 0 12 12"><path d="M2.5 0.5 4.5 3 3.3 4.6a7 7 0 0 0 4.1 4.1L9 7.5l2.5 2-1 2C5 11.5.5 7 .5 1.5Z" fill="#fff"/></svg><span>+39 055 0102030</span></div>
  <div class="contact-line"><svg width="13" height="10" viewBox="0 0 13 10"><rect x=".5" y=".5" width="12" height="9" fill="#fff"/><path d="m.5.8 6 4.5 6-4.5" fill="none" stroke="#1b1f1e" stroke-width="1"/></svg><span>hello@staynest.example</span></div>
</div>
<div class="abs fcol" style="left:992px;top:4920px">
  <h6>Follow Us</h6>
  <div class="social"><i></i>Chatterbox</div>
  <div class="social"><i></i>Birdline</div>
  <div class="social"><i></i>Snapgram</div>
</div>
<p class="abs copyright">Copyright © 2021 <b>StayNest</b>. All rights reserved.</p>

</body>
</html>
```